Homeward Sale Co website

i need a website that is to get customers to let us sell their house within 30 days with no sales fees based in the uk. iv uploaded a design i like for the website i own i want a copy of this but for the different logo ect need the house buying logo i own to be changed to Homeward Sale Co
it needs to be able to flash up to sell your house today contact box to collect their details such as property type, address, number of bedrooms, (estate agents valuation) , best price you can accept after they have seen the main section banner with advertising why use us.
the three reasons in the banner to use us needs to be
1: We will sell your house in 30 days and ensure we take a buyers fee for our service from the buyer meaning your buyer is secured unlike with most estate agents
2: We do not charge you any fees at all! our small fee is charged to the buyer
3: A huge network of investors and private buyers connecting many estate agents, auction houses, investors, and private buyers to ensure a fast sale.

```html
<!DOCTYPE html>
<html lang="en">
<head>
<meta charset="utf-8">
<title>Homeward Sale Co</title>
<link href="https://fonts.googleapis.com/css2?family=Questrial&family=Quicksand:wght@600;700&display=swap" rel="stylesheet">
<style>
:root{
  --night:#050b26;
  --night-2:#1c2a5c;
  --brand:#1e8bd3;
  --brand-dark:#2a63b8;
  --ink:#222;
  --muted:#555;
  --grey-btn:#4a4a4a;
  --panel:#f4f4f4;
  --footer:#082a44;
  --white:#fff;
}
*{box-sizing:border-box;margin:0;padding:0}
html,body{width:720px;height:1200px;overflow:hidden}
body{font-family:"Questrial",sans-serif;color:var(--ink);background:var(--white);position:relative}
.abs{position:absolute}
.hero{left:0;top:0;width:720px;height:463px;background:linear-gradient(180deg,var(--night) 0%,var(--night-2) 60%,#24346a 100%);overflow:hidden}
.brand-name{font-family:"Questrial",sans-serif;color:var(--brand);font-size:15px;letter-spacing:.2px;display:flex;align-items:center;gap:6px}
.brand-name .dot{width:10px;height:10px;border-radius:50%;background:var(--brand)}
.hero .brand-name{left:72px;top:48px}
.btn{display:flex;align-items:center;justify-content:center;gap:4px;color:var(--white);font-size:8px;border-radius:3px}
.login{left:524px;top:32px;width:55px;height:20px;background:var(--grey-btn)}
.register{left:585px;top:32px;width:63px;height:20px;background:var(--brand)}
.hero-title{left:0;top:130px;width:720px;text-align:center;font-family:"Quicksand",sans-serif;font-weight:700;font-size:13px;color:var(--brand)}
.search{left:144px;top:154px;width:432px;height:70px;background:var(--brand);border-radius:3px;opacity:.92}
.field{top:10px;width:111px}
.field label{display:block;font-family:"Quicksand",sans-serif;font-weight:700;font-size:6.5px;color:var(--white);margin-bottom:3px}
.field .box{height:19px;background:var(--white);border-radius:2px;font-size:6.5px;color:#777;padding:0 8px;display:flex;align-items:center;justify-content:space-between}
.caret{width:0;height:0;border-left:2.5px solid transparent;border-right:2.5px solid transparent;border-top:3px solid #444}
.search-btn{left:368px;top:21px;width:48px;height:19px;background:#1a9be0;border-radius:2px;color:var(--white);font-family:"Quicksand",sans-serif;font-weight:700;font-size:6.5px;display:flex;align-items:center;justify-content:center}
.search-note{left:0;top:50px;width:432px;text-align:center;color:var(--white);font-size:9px}
.tenant{left:268px;top:236px;width:185px;height:20px;background:var(--grey-btn);border-radius:3px;color:var(--white);font-size:7.5px;display:flex;align-items:center;justify-content:center}
.street{left:0;top:262px;width:720px;height:201px;background:linear-gradient(180deg,rgba(28,42,92,0) 0%,#2c3c7a 30%,#6b4a6a 60%,#8e9b3a 88%,#c9a94a 100%)}
.why{left:0;top:463px;width:720px;height:303px}
.sec-title{width:720px;text-align:center;font-family:"Quicksand",sans-serif;font-weight:700;color:var(--brand-dark)}
.why .sec-title{top:48px;font-size:19px}
.underline{height:1.5px;background:var(--brand-dark)}
.why .underline{left:335px;top:71px;width:43px}
.why .sub{top:80px;width:720px;text-align:center;font-size:8px;color:var(--muted)}
.card{top:109px;width:160px;height:151px;background:#f7f7f7;box-shadow:0 0 4px rgba(0,0,0,.12);border-radius:3px;text-align:center;padding:0 8px}
.card .num{margin:16px auto 20px;width:36px;height:36px;border-radius:50%;background:var(--brand);color:var(--white);font-family:"Quicksand",sans-serif;font-weight:700;font-size:12px;display:flex;align-items:center;justify-content:center}
.card p{font-size:8px;line-height:11.3px;color:var(--ink)}
.card strong{display:block;font-family:"Quicksand",sans-serif;font-weight:700;color:var(--brand-dark);font-size:9px;letter-spacing:.2px}
.touch{left:0;top:766px;width:720px;height:277px;background:var(--panel)}
.touch .sec-title{top:32px;font-size:20px}
.touch .underline{left:346px;top:57px;width:36px}
.form-field{width:150px}
.form-field.half{width:72px}
.form-field label{display:block;font-size:7px;color:var(--muted);margin-bottom:2px;padding-left:1px;white-space:nowrap}
.form-field .input{height:19px;background:var(--white);border:1px solid #e2e2e2;border-radius:2px;display:flex;align-items:center;justify-content:flex-end;padding-right:6px}
.submit{left:332px;top:161px;width:55px;height:19px;background:var(--grey-btn);color:var(--white);border-radius:3px;font-size:7.5px;display:flex;align-items:center;justify-content:center}
.skyline{left:0;top:209px;width:720px;height:68px;background:linear-gradient(180deg,var(--panel) 0%,#b9c3cc 40%,var(--footer) 100%)}
.footer{left:0;top:1043px;width:720px;height:137px;background:var(--footer)}
.footer .brand-name{left:72px;top:72px;font-size:14px}
.foot-col h3{font-family:"Quicksand",sans-serif;font-weight:700;color:var(--brand);font-size:9px;margin-bottom:9px}
.foot-col li{list-style:none;color:var(--white);font-size:7px;line-height:12.4px}
.foot-col .first{color:var(--brand);text-decoration:underline}
.contact li{display:flex;align-items:center;gap:6px;line-height:19.5px}
.contact svg{width:8px;height:8px;flex:none}
.bar{left:0;top:1180px;width:720px;height:20px;background:var(--brand);color:var(--white);font-size:6.5px}
.bar .copy{left:72px;top:6px}
.social{top:4px;width:12px;height:12px;border-radius:50%;background:var(--white)}
</style>
</head>
<body>

<section class="hero abs">
  <div class="brand-name abs"><span class="dot"></span>Homeward Sale Co</div>
  <a class="btn login abs">
    <svg width="7" height="7" viewBox="0 0 10 10" fill="none" stroke="#fff" stroke-width="1.2"><circle cx="5" cy="5" r="4"/><path d="M3 5h4M5.5 3.5 7 5 5.5 6.5"/></svg>Login</a>
  <a class="btn register abs">
    <svg width="7" height="7" viewBox="0 0 10 10" fill="none" stroke="#fff" stroke-width="1.2"><circle cx="5" cy="3.2" r="2.2"/><path d="M1.5 9.5c0-2 1.6-3.3 3.5-3.3s3.5 1.3 3.5 3.3"/></svg>Register</a>
  <h1 class="hero-title abs">The Fastest way to swap your social home</h1>
  <form class="search abs">
    <div class="field abs" style="left:16px"><label>Location</label><div class="box">Twown or post code<span class="caret"></span></div></div>
    <div class="field abs" style="left:133px"><label>Bedrooms</label><div class="box">Any</div></div>
    <div class="field abs" style="left:250px"><label>Max. Rent ($ Per month)</label><div class="box">Any<span class="caret"></span></div></div>
    <div class="search-btn abs">SEARCH</div>
    <p class="search-note abs">Join 500,000 other social tenants on Homeward</p>
  </form>
  <a class="tenant abs">Are you a tenant? Click here for more info</a>
  <div class="street abs" role="img" aria-label="Illustrated night sky with moon over a street of houses with residents and speech bubbles: I want to downsize, We need to be nearer family, I need more space"></div>
</section>

<section class="why abs">
  <h2 class="sec-title abs">Why Choose Us</h2>
  <div class="underline abs"></div>
  <p class="sub abs">The UK's leading mutual exchange service for social housing</p>
  <article class="card abs" style="left:104px">
    <div class="num">01</div>
    <p>We will<strong>SELL YOUR HOUSE IN 30 DAYS</strong>and ensure we take a buyers fee for our service from the buyer meaning your buyer is secured unlike with most estate agents</p>
  </article>
  <article class="card abs" style="left:280px">
    <div class="num">02</div>
    <p><strong>WE DO NOT CHARGE</strong>you any fees at all! our small fee is charged to the buyer</p>
  </article>
  <article class="card abs" style="left:456px">
    <div class="num">03</div>
    <p><strong>A HUGE NETWORK</strong>of investors and private buyers connecting many estate agents, auction houses, investors, and private buyers to ensure a fast sale.</p>
  </article>
</section>

<section class="touch abs">
  <h2 class="sec-title abs">Get In Touch</h2>
  <div class="underline abs"></div>
  <div class="form-field abs" style="left:122px;top:74px"><label>Name</label><div class="input"></div></div>
  <div class="form-field abs" style="left:285px;top:74px"><label>Email</label><div class="input"></div></div>
  <div class="form-field abs" style="left:448px;top:74px"><label>Property Address</label><div class="input"></div></div>
  <div class="form-field abs" style="left:122px;top:115px"><label>Property Type</label><div class="input"><span class="caret"></span></div></div>
  <div class="form-field abs" style="left:285px;top:115px"><label>Bedrooms</label><div class="input"><span class="caret"></span></div></div>
  <div class="form-field half abs" style="left:448px;top:115px"><label>Agent Valuation (£)</label><div class="input"></div></div>
  <div class="form-field half abs" style="left:526px;top:115px"><label>Best Price (£)</label><div class="input"></div></div>
  <a class="submit abs">Submit</a>
  <div class="skyline abs" role="img" aria-label="City skyline silhouette with clock tower and observation wheel"></div>
</section>

<footer class="footer abs">
  <div class="brand-name abs"><span class="dot"></span>Homeward Sale Co</div>
  <div class="foot-col contact abs" style="left:252px;top:35px">
    <h3>Contact Us</h3>
    <ul>
      <li><svg viewBox="0 0 10 10"><path d="M5 0.5a3.3 3.3 0 0 0-3.3 3.3C1.7 6.2 5 9.5 5 9.5s3.3-3.3 3.3-5.7A3.3 3.3 0 0 0 5 .5z" fill="#1e8bd3"/><circle cx="5" cy="3.8" r="1.2" fill="#082a44"/></svg>27 Maple Row, Ashford, AB1 2CD</li>
      <li><svg viewBox="0 0 10 10"><path d="M2 .8 3.8 3 2.9 4.2a6 6 0 0 0 2.9 2.9L7 6.2 9.2 8 8 9.3C4.5 9 1 5.5.7 2z" fill="#1e8bd3"/></svg>01-234-567-890</li>
      <li><svg viewBox="0 0 10 10"><rect x=".5" y="2" width="9" height="6" fill="#1e8bd3"/><path d="M.5 2 5 5.5 9.5 2" stroke="#082a44" fill="none"/></svg>hello@homewardsale.com</li>
    </ul>
  </div>
  <div class="foot-col abs" style="left:451px;top:35px">
    <h3>Quick Links</h3>
    <ul><li class="first">Home</li><li>About</li><li>Accessibility</li><li>FAQ'S</li><li>Get in touch</li></ul>
  </div>
  <div class="foot-col abs" style="left:550px;top:35px">
    <h3>Advice &amp; tips</h3>
    <ul><li>Blog</li><li>Careers</li><li>Privacy</li><li>Terms</li></ul>
  </div>
</footer>

<div class="bar abs">
  <p class="copy abs">© 2023 Homeward Sale Co. All Right Reserved</p>
  <span class="social abs" style="left:584px"></span>
  <span class="social abs" style="left:601px"></span>
  <span class="social abs" style="left:618px"></span>
  <span class="social abs" style="left:635px"></span>
</div>

</body>
</html>
```